Postcard needed for expert witness service

Looking for a professional postcard that will be mailed to personal injury lawyers / law firms to introduce my expert witness services.

Target Market(s)

Law firms, personal injury lawyers

Industry/Entity Type

Expert witness, law

Font styles to use
Sans Serif

Requirements
Must have
• Logo: The Frost Counsel [Main Heading]Do you handle snow and ice related slip and falls? Darrel is one of the top snow industry experts in the country! [Following should be in a list type fashion, possibly bulleted]Darrel's credentials: Accredited Winter Practitioner (AWP), past WRTA board member and chair, former ISO 9001 certified snow company owner , 32 years in the industry. (555) 284-3917 NOTES: Postcard will be 4" x 6" Please use both sides however must have room for labels and stamp
Should not have
• Wouldn't suggest using both photos on same side. Honestly, feel free to only use one of the slip and fall photos if it works out better. Thanks!

```html
<!DOCTYPE html>
<html lang="en">
<head>
<meta charset="utf-8">
<title>The Frost Counsel – Postcard</title>
<link href="https://fonts.googleapis.com/css2?family=Roboto+Condensed:wght@300;700&display=swap" rel="stylesheet">
<style>
  :root {
    --brand-blue: #0096d9;
    --paper: #ffffff;
    --page: #ffffff;
    --rule: #9a9a9a;
    --shadow: rgba(0,0,0,0.28);
    --photo-snow: #e9ecef;
    --photo-gravel: #9b9186;
    --photo-coat: #4a3a35;
  }
  html, body {
    margin: 0;
    padding: 0;
    width: 933px;
    height: 1200px;
    overflow: hidden;
    background: var(--page);
    font-family: "Roboto Condensed", "Arial Narrow", sans-serif;
  }
  .canvas { position: relative; width: 933px; height: 1200px; }

  .postcard {
    position: absolute;
    left: 65px;
    width: 800px;
    height: 532px;
    background: var(--paper);
    box-shadow: 2px 2px 3px var(--shadow);
    overflow: hidden;
  }
  .postcard--front { top: 58px; }
  .postcard--back { top: 622px; }

  /* Front */
  .hero-photo {
    position: absolute; inset: 0;
    background:
      radial-gradient(ellipse at 45% 40%, var(--photo-coat) 0%, rgba(74,58,53,0.85) 22%, rgba(74,58,53,0) 45%),
      radial-gradient(ellipse at 80% 25%, var(--photo-snow) 0%, rgba(233,236,239,0) 55%),
      radial-gradient(ellipse at 75% 85%, #6c7a8c 0%, rgba(108,122,140,0) 40%),
      linear-gradient(160deg, var(--photo-gravel) 0%, #b9b2a8 40%, var(--photo-snow) 70%, #d6d8da 100%);
  }
  .torn-band { position: absolute; left: 0; top: 0; width: 800px; height: 532px; }
  .brand-front {
    position: absolute;
    left: 26px; top: 20px;
    color: var(--paper);
    font-weight: 300;
    font-size: 34px;
    letter-spacing: 1px;
    line-height: 1;
    margin: 0;
  }
  .headline {
    position: absolute;
    left: 0; right: 0; top: 265px;
    margin: 0;
    text-align: center;
    color: var(--brand-blue);
    font-weight: 700;
    font-size: 58px;
    line-height: 54px;
    letter-spacing: 0;
  }

  /* Back */
  .blue-panel { position: absolute; left: 0; top: 0; width: 800px; height: 532px; }
  .credentials {
    position: absolute;
    left: 0; top: 30px; width: 418px;
    color: var(--paper);
    text-align: center;
  }
  .credentials__title {
    margin: 0;
    font-weight: 700;
    font-size: 48px;
    line-height: 44px;
  }
  .credentials__list {
    list-style: none;
    margin: 24px 0 0;
    padding: 0;
    font-weight: 700;
    font-size: 23px;
    line-height: 22px;
  }
  .credentials__list li { margin-bottom: 12px; }
  .credentials__list li::before {
    content: "";
    display: inline-block;
    width: 10px; height: 10px;
    border-radius: 50%;
    background: var(--paper);
    margin-right: 7px;
    vertical-align: 3px;
  }
  .brand-back {
    position: absolute;
    left: 0; width: 418px; top: 392px;
    margin: 0;
    text-align: center;
    color: var(--paper);
    font-weight: 300;
    font-size: 30px;
    letter-spacing: 1px;
  }
  .phone {
    position: absolute;
    left: 0; width: 418px; top: 448px;
    display: flex; align-items: center; justify-content: center; gap: 8px;
    color: var(--paper);
    font-weight: 700;
    font-size: 44px;
    line-height: 1;
  }
  .phone svg { width: 30px; height: 30px; }
  .stamp-box {
    position: absolute;
    left: 652px; top: 80px;
    width: 77px; height: 84px;
    border: 1px solid var(--rule);
  }
  .address-line {
    position: absolute;
    left: 482px; width: 248px;
    height: 0;
    border-top: 1px solid var(--rule);
  }
</style>
</head>
<body>
<div class="canvas">

  <section class="postcard postcard--front">
    <div class="hero-photo" role="img" aria-label="Photo of a woman in a knit hat and dark coat slipping and falling on an icy, snowy gravel path"></div>
    <svg class="torn-band" viewBox="0 0 800 532" aria-hidden="true">
      <polygon fill="#ffffff" points="0,252 30,250 55,247 80,250 110,246 140,249 170,244 200,246 225,240 250,244 280,236 305,240 330,231 360,234 390,236 420,240 450,232 480,234 505,238 535,233 560,236 590,230 620,233 650,238 680,235 710,240 740,242 770,246 800,248 800,398 770,400 740,394 710,398 680,392 650,396 625,390 600,392 570,398 545,394 515,398 490,402 460,400 430,404 400,400 370,406 340,402 310,408 280,404 250,410 220,406 190,412 160,408 130,414 100,410 70,404 40,408 20,404 0,406"/>
    </svg>
    <p class="brand-front">THE FROST COUNSEL</p>
    <h1 class="headline">DO YOU HANDLE SNOW AND ICE<br>RELATED SLIP AND FALLS?</h1>
  </section>

  <section class="postcard postcard--back">
    <svg class="blue-panel" viewBox="0 0 800 532" aria-hidden="true">
      <polygon fill="var(--brand-blue)" points="0,0 418,0 416,20 422,40 420,60 428,80 432,100 436,120 432,140 438,160 434,180 440,200 436,220 432,240 438,260 434,280 428,300 432,320 436,340 430,360 436,380 432,400 428,420 420,440 424,460 416,480 420,500 414,520 418,532 0,532"/>
    </svg>
    <div class="credentials">
      <h2 class="credentials__title">DARREL'S<br>CREDENTIALS</h2>
      <ul class="credentials__list">
        <li>Accredited Winter<br>Practitioner (AWP)</li>
        <li>Past WRTA board<br>member and chair</li>
        <li>Former ISO 9001 Certified<br>snow company owner</li>
        <li>32 years in the industry</li>
      </ul>
    </div>
    <p class="brand-back">THE FROST COUNSEL</p>
    <div class="phone">
      <svg viewBox="0 0 24 24" aria-hidden="true"><path fill="#ffffff" d="M6.6 10.8c1.4 2.8 3.8 5.1 6.6 6.6l2.2-2.2c.3-.3.7-.4 1-.2 1.1.4 2.3.6 3.6.6.6 0 1 .4 1 1V20c0 .6-.4 1-1 1C10.6 21 3 13.4 3 4c0-.6.4-1 1-1h3.5c.6 0 1 .4 1 1 0 1.3.2 2.5.6 3.6.1.3 0 .7-.2 1L6.6 10.8z"/></svg>
      <span>(555) 284-3917</span>
    </div>
    <div class="stamp-box"></div>
    <div class="address-line" style="top:244px"></div>
    <div class="address-line" style="top:298px"></div>
    <div class="address-line" style="top:352px"></div>
    <div class="address-line" style="top:406px"></div>
  </section>

</div>
</body>
</html>
```